Für das neue Tantra-Bildungszetrum: 8-oder 10-Seiten-Faltblatt und ein Plakat DIN A3
Zielgruppe
Es geht darum, über das Angebot des neuen Bildungszentrums Kreis der Morgenröte zu informieren.
Das Zentrum organisiert und führt regelmäßige Veranstaltungen wie Info-Vorträge, Schnuppertage, Seminare, Kurse und Intensivtrainings durch, ist in allem spezialisiert auf Tantra. Das Zentrum ist vertreten an mehreren Standorten Deutschlands durch das jeweils ein Team an Lehrern und Dozenten. Für die Veranstaltungen werden externe Räume angemietet. Das Angebot soll in jeder Stadt, wo die Broschüren oder Faltblätter verteilt werden. Die Anmeldung und Registrierung erfolgt über die neue Homepage, die bald freigegeben wird und noch nicht zur Verfügung steht.
Das Besondere am Zentrum ist die Möglichkeit, eigene tantrische Selbsterfahrungen zu machen und entweder später oder als Option sich gleich für einen der sechs neuen Tantra- Ausbildungsberufe zu entscheiden.
Darüber hinaus, soll die Broschüre oder die Faltblätter zur Mitarbeit und Kooperation mit selbständigen Yoga- und Tantra-Lehrern, sowie Ärzten, Therapeuten und Heilpraktiken einladen.
Das Bildungszentrum ist ein Netzwerk der Honorar-Dozenten, die entweder Lehrer und Experte auf dem tantrischen Bereich oder Vertreter der klassischen und alternativen Heilkunde oder beides zusammen sind.
Wer ist die Zielgruppe? Männer und Frauen, vom 18 - 60 Jahre. Menschen, die sich für Tantra und Selbsterfahrung interessieren, und Menschen, die nach einer neuen beruflichen Perspektive suchen.
Aufgabenstellung
1). 10-Seiten- Faltblatt designen
2). Plakat DIN A3 gestalten

```html
<!DOCTYPE html>
<html lang="de">
<head>
<meta charset="utf-8">
<title>Bildungszentrum Kreis der Morgenröte – Plakat</title>
<link rel="stylesheet" href="https://fonts.googleapis.com/css2?family=Alegreya+Sans:wght@700&family=Noto+Serif:wght@400&family=PT+Sans:wght@400;700&display=swap">
<style>
  :root {
    --green: #2c6c52;
    --orange: #e8711c;
    --orange-soft: #f3b07a;
    --panel: #e8eeeb;
    --ink: #1f2a24;
    --white: #ffffff;
  }
  html, body { margin: 0; padding: 0; overflow: hidden; background: var(--white); }
  .poster {
    position: relative; width: 849px; height: 1200px; overflow: hidden;
    background: var(--white); color: var(--ink);
    font-family: "PT Sans", Arial, sans-serif;
  }
  .brand-dot {
    position: absolute; left: 165px; top: 68px; width: 86px; height: 86px;
    border-radius: 50%; background: var(--orange);
  }
  .brand-name {
    position: absolute; left: 270px; top: 62px; margin: 0;
    font-family: "Alegreya Sans", Arial, sans-serif; font-weight: 700; color: var(--green);
    font-size: 40px; line-height: 48px; white-space: nowrap;
  }
  .intro-panel { position: absolute; left: 0; top: 180px; width: 849px; height: 420px; }
  .intro-text {
    position: absolute; left: 34px; top: 266px; width: 642px; margin: 0;
    font-family: "Noto Serif", Georgia, serif; font-size: 15.4px; line-height: 21.3px;
    text-align: justify; hyphens: auto; color: var(--ink);
  }
  .intro-text .initial {
    float: left; font-size: 46px; line-height: 38px; color: var(--orange);
    margin: 3px 3px 0 0;
  }
  .intro-photo {
    position: absolute; left: 690px; top: 250px; width: 159px; height: 330px;
    border-radius: 50% 0 0 50% / 50% 0 0 50%;
    background: radial-gradient(circle at 70% 50%, #c98a6a 0%, #9b4a2e 45%, #e8711c 75%, #f3a55c 100%);
  }
  .ornament {
    position: absolute; border-radius: 50%;
    background: radial-gradient(circle, var(--orange-soft) 0%, #f8d6b8 60%, #fbe7d6 100%);
  }
  .block {
    position: absolute; font-size: 14.5px; line-height: 21.5px; font-weight: 700;
    color: var(--green); white-space: nowrap;
  }
  .block p { margin: 0; }
  .block .accent { color: var(--orange); }
  .block ol, .block ul { margin: 0; padding: 0; list-style: none; font-weight: 400; color: var(--ink); }
  .divider { position: absolute; height: 2px; background: var(--green); }
  .network {
    position: absolute; left: 95px; top: 935px; width: 380px; margin: 0; text-align: center;
    font-size: 20px; line-height: 27px; font-weight: 700; color: var(--green);
  }
  .contact-band { position: absolute; left: 0; top: 1050px; width: 849px; height: 150px; }
  .contact-title {
    position: absolute; left: 356px; top: 1004px; margin: 0;
    font-size: 20px; line-height: 26px; font-weight: 700; color: var(--green);
  }
  .contact-list { position: absolute; left: 322px; top: 1058px; margin: 0; padding: 0; list-style: none; }
  .contact-list li {
    display: flex; align-items: center; gap: 13px; height: 35px;
    font-size: 17px; font-weight: 700; color: var(--white); white-space: nowrap;
  }
  .contact-list svg { width: 22px; height: 22px; flex: none; }
  .contact-list .dot { width: 20px; height: 20px; border-radius: 50%; background: var(--white); flex: none; margin: 0 1px; }
  .team-photo {
    position: absolute; left: 205px; top: 1028px; width: 120px; height: 150px; border-radius: 50%;
    border: 4px solid var(--white); box-sizing: border-box;
    background: radial-gradient(circle at 50% 45%, #b28b72 0%, #6b4a38 55%, #3c2d25 100%);
  }
</style>
</head>
<body>
<div class="poster">

  <span class="brand-dot" aria-hidden="true"></span>
  <p class="brand-name">Bildungszentrum<br>Kreis der Morgenröte</p>

  <svg class="intro-panel" viewBox="0 0 849 420" width="849" height="420" aria-hidden="true">
    <rect x="0" y="25" width="849" height="375" fill="var(--panel)"/>
    <path d="M0 0 H849 V20 C620 -5 300 70 0 40 Z" fill="var(--white)"/>
    <path d="M0 20 C300 48 560 -8 849 2 V28 C600 14 300 72 0 48 Z" fill="var(--green)"/>
    <path d="M0 402 C300 382 560 417 849 397 V420 H0 Z" fill="var(--white)"/>
    <path d="M0 402 C300 382 560 417 849 397" fill="none" stroke="var(--green)" stroke-width="5"/>
  </svg>

  <p class="intro-text"><span class="initial">U</span>nser Bildungszentrum soll viele Menschen bei ihren inneren Transformationsprozessen unterstützen indem es spezielle berufliche Perspektiven anbietet, bei denen Selbstverwirklichung in authentischem Kontakt mit anderen Menschen möglich ist. Wenn die innere Welt in Frieden, Harmonie und Ruhe ist, so wird sich dies auch auf unsere äußere Welt auswirken und initiiert so einen Gesellschaftswandel durch innere Transformation. Tantra liefert uns Techniken, die unser Bewusstsein durch die Transformation innerer Vorgänge grundlegend wandeln. Tantra unterstützt Menschen in ihrem Bemühen um spirituelles Wachstum, Selbstverwirklichung, innere Entwicklung sowie der Verbesserung ihrer Liebes- und Lustfähigkeit. Es fördert das Aufblühen der eigenen Göttlichkeit und das Nutzen von sexueller Energie im spirituellen Sinne. Dies ist nur kleiner Ausschnitt dessen, was Tantra uns ermöglicht.</p>

  <div class="intro-photo" role="img" aria-label="Foto eines Paares in warmem Licht, gerahmt von einem orangefarbenen Mandala-Ornament"></div>

  <div class="ornament" style="left:32px;top:680px;width:82px;height:82px" role="img" aria-label="Orangefarbenes Yantra-Ornament"></div>
  <div class="block" style="left:162px;top:645px">
    <p>Wir laden dich herzlich zu unseren<br><span class="accent">regelmäßigen Vorträgen</span> ein:</p>
    <ol><li>1. Was ist Tantra?</li><li>2. Berufliche Perspektiven mit Tantra.</li></ol>
  </div>
  <div class="divider" style="left:162px;top:737px;width:232px"></div>

  <div class="ornament" style="left:30px;top:830px;width:84px;height:90px" role="img" aria-label="Orangefarbenes Yantra-Ornament"></div>
  <div class="block" style="left:162px;top:795px">
    <p>Steige ein in den nächsten<br><span class="accent">12- Wochen Tantra-Kurs:</span></p>
    <ul style="margin-top:18px;padding-left:10px;line-height:19.5px">
      <li>•&nbsp; "Tantra für Anfänger"</li>
      <li>•&nbsp; "Tantra für Mittelstufe"</li>
      <li>•&nbsp; "Tantra für Fortgeschrittene"</li>
    </ul>
  </div>

  <div class="ornament" style="left:427px;top:627px;width:70px;height:78px" role="img" aria-label="Orangefarbenes Yantra-Ornament"></div>
  <div class="block" style="left:532px;top:624px;line-height:24px">
    <p>Erfahre den Geschmack, den Geruch,<br>die Farbe und den Klang von Tantra<br>bei einem unserer <span class="accent">Schnuppertage</span><br><span class="accent">oder Einsteiger-Wochenenden.</span></p>
  </div>
  <div class="divider" style="left:532px;top:737px;width:278px"></div>

  <div class="ornament" style="left:423px;top:758px;width:87px;height:90px" role="img" aria-label="Orangefarbenes Yantra-Ornament"></div>
  <div class="block" style="left:532px;top:759px;line-height:24px">
    <p>Mach Tantra zu deinem Beruf!<br>Investiere zwei bis fünf wundervolle<br>Jahre je nach deiner Wahl in eine<br><span class="accent">Berufsausbildung mit Zukunft!</span><br>Welche unserer sechs Ausbildungs-<br>berufe spricht dich an?</p>
    <ol style="margin-top:16px;line-height:19.5px">
      <li>1. Tantra-Lehrer</li>
      <li>2. Tantra-Yoga-Lehrer</li>
      <li>3. Tantrischer Massagetherapeut</li>
      <li>4. Tantrischer Sexualtherapeut</li>
      <li>5. Tantra-Coach</li>
      <li>6. Selbst Ausbilder werden</li>
    </ol>
  </div>

  <p class="network">Wir sind ein wachsendes<br>Netzwerk aus mehreren Lehrern.</p>

  <svg class="contact-band" viewBox="0 0 849 150" width="849" height="150" aria-hidden="true">
    <path d="M306 0 H849 V150 H296 Z" fill="var(--green)"/>
  </svg>
  <div class="team-photo" role="img" aria-label="Porträtfoto einer Lehrerin des Zentrums"></div>
  <h2 class="contact-title">Kontakt:</h2>
  <ul class="contact-list">
    <li>
      <svg viewBox="0 0 24 24" aria-hidden="true"><circle cx="12" cy="12" r="10" fill="none" stroke="#fff" stroke-width="2"/><ellipse cx="12" cy="12" rx="4.5" ry="10" fill="none" stroke="#fff" stroke-width="1.6"/><path d="M2 12 H22 M4 7 H20 M4 17 H20" stroke="#fff" stroke-width="1.4"/></svg>
      www.morgenroete-kreis.de
    </li>
    <li>
      <svg viewBox="0 0 24 24" aria-hidden="true"><path d="M6.6 10.8a15.1 15.1 0 0 0 6.6 6.6l2.2-2.2a1 1 0 0 1 1-.25 11.4 11.4 0 0 0 3.6.57 1 1 0 0 1 1 1V20a1 1 0 0 1-1 1A17 17 0 0 1 3 4a1 1 0 0 1 1-1h3.5a1 1 0 0 1 1 1c0 1.25.2 2.45.57 3.57a1 1 0 0 1-.25 1z" fill="#fff"/></svg>
      0176 31 52 74 08
    </li>
    <li><span class="dot" aria-hidden="true"></span>Tantrisches.Bildungszentrum.KreisDerMorgenroete</li>
    <li><span class="dot" aria-hidden="true"></span>KreisDerMorgenroete</li>
  </ul>

</div>
</body>
</html>
```